Flyer-Design für Karin Dossow
Zielgruppe
Ich bin psychologische Beraterin und Heilpraktikerin für Psychotherapie. Ich biete ein Coaching speziell für Mütter (meist Mütter mit neugeborenen Babys) an. Dieses Mütter-Coaching will ich bewerben. Die Flyer werden unter anderen an Ärzte und Hebammen weiter gegeben und dort in den Praxen ausliegen.
Aufgabenstellung
In meinem Logo herrschen die Farben orange und grau vor - es wäre schön, wenn sich diese Farben im Flyer wiederfinden würden - evtl. kombiniert mit mittelblau oder einem hellem grün.
Des weiteren möchte ich später Flyer im Din Lang Format (einseitig) mit anderen Angeboten erstellen. Das sollte mit dem Design dann auch möglich sein.
Der Schrifttyp soll bitte Arial sein, passend zum Logo. Ich habe bei Bildarko Fotos zu dem Thema erstanden, die ich stimmig finde. Diese Bilder sollten im Flyer genutzt werden.
Für diesen Flyer hätte ich gerne das Format: Falzblatt mit Wickelfalz - 279 x 219 mm

```html
<!DOCTYPE html>
<html lang="de">
<head>
<meta charset="utf-8">
<title>Karin Dossow – Coaching für Mütter</title>
<link href="https://fonts.googleapis.com/css2?family=Arimo:wght@400;700&display=swap" rel="stylesheet">
<style>
  :root {
    --backdrop: #e9e7e4;
    --paper: #ececeb;
    --photo-light: #eceee6;
    --photo-mid: #c9b8a8;
    --photo-dark: #4a3c36;
    --ink: #1f1f1f;
    --logo-grey: #8c8c8c;
    --orange: #e8a23e;
    --blue: #62b2e3;
    --white: #ffffff;
  }
  * { margin: 0; padding: 0; box-sizing: border-box; }
  html, body {
    width: 1200px; height: 835px; overflow: hidden;
    background: var(--backdrop);
    font-family: "Arimo", Arial, sans-serif;
  }
  .flyer-cover {
    position: absolute; left: 410px; top: 22px;
    width: 380px; height: 790px;
    background: var(--paper);
    box-shadow: 0 6px 24px rgba(0,0,0,.18);
    overflow: hidden;
  }
  .cover-shapes { position: absolute; inset: 0; }
  .headline {
    position: absolute; left: 38px; top: 392px;
    font-size: 29px; line-height: 1.38; font-weight: 400;
    color: var(--ink); text-transform: uppercase; letter-spacing: -0.5px;
  }
  .headline strong { font-weight: 700; }
  .brand-name {
    position: absolute; left: 40px; top: 592px;
    font-size: 31px; font-weight: 400; color: var(--logo-grey);
    letter-spacing: -0.5px;
  }
  .offer {
    position: absolute; left: 32px; top: 670px; color: var(--white);
  }
  .offer-title { font-size: 18px; font-weight: 700; text-transform: uppercase; letter-spacing: -0.3px; }
  .offer-pillars { font-size: 10.5px; font-weight: 400; text-transform: uppercase; margin-top: 3px; letter-spacing: .2px; }
</style>
</head>
<body>
  <section class="flyer-cover">
    <svg class="cover-shapes" width="380" height="790" viewBox="0 0 380 790">
      <defs>
        <linearGradient id="photoTone" x1="0" y1="0" x2="1" y2="1">
          <stop offset="0" stop-color="var(--photo-light)"/>
          <stop offset=".55" stop-color="var(--photo-mid)"/>
          <stop offset="1" stop-color="var(--photo-dark)"/>
        </linearGradient>
      </defs>
      <path role="img" aria-label="Foto: Mutter hält ihr schlafendes Baby an der Schulter"
            fill="url(#photoTone)"
            d="M0 0 H380 V372 C300 330 160 330 0 378 Z"/>
      <path class="band-orange" fill="var(--orange)"
            d="M0 630 C140 626 280 660 380 700 V790 H0 Z"/>
      <path class="band-blue" fill="var(--blue)"
            d="M0 714 C130 720 260 752 330 790 H0 Z"/>
    </svg>

    <h1 class="headline">Das Baby ist da<br>und <strong>nichts</strong><br>ist mehr<br>wie es war!</h1>

    <div class="brand-name">karindossow</div>

    <div class="offer">
      <p class="offer-title">Coaching für Mütter</p>
      <p class="offer-pillars">Begleitung - Stärkung - Beratung</p>
    </div>
  </section>
</body>
</html>
```